Redesign of Smart Watch Gift Voucher-SEE ATTACHED CURRENT DESIGN

I need to redesign my existing design using all same content and elements.

MY ENVISION: I invision more of a professional advertisement type of flyer/voucher. Imagine how Corvel.com would create a professionally looking flyer promoting the lumo or veno.

you can get many ideas about professional design by looking at some of corvels flyer designs :
https://www.findora-example.net/search?q=lumo+advertisment&mode=img&ref=a83kd02mzq7

stock photos are attached, you do not have to use them all, you can use some or none i am open to your designs using your own images if you want...just make sure the smartwatch looks black

DO NOT LEAVE ANY CONTENT OR ELEMENTS OUT ON MOCK UP PLEASE

SEE ATTACHED CURRENT DESIGN

I need to redesign my existing design using all same content and elements. DO NOT LEAVE ANY CONTENT OR ELEMENTS OUT ON MOCK UP PLEASE

Target Market(s)

B2B-you can get many ideas about professional design by looking at some of corvels flyer designs :

Industry/Entity Type

Marketing

Requirements
Must have
• I need to redesign my existing design using all same content and elements. DO NOT LEAVE ANY CONTENT OR ELEMENTS OUT ON MOCK UP PLEASE

Nice to have

Should not have

```html
<!DOCTYPE html>
<html lang="en">
<head>
<meta charset="utf-8">
<title>Smart Fitness Watch Voucher</title>
<link href="https://fonts.googleapis.com/css2?family=Oswald:wght@400;500;600;700&family=Open+Sans:ital,wght@0,400;0,600;0,700;1,700&display=swap" rel="stylesheet">
<style>
  :root{
    --backdrop:#6b6b6b;
    --paper:#ffffff;
    --paper-shade:#e9eaec;
    --red:#c4161c;
    --red-deep:#8e0d12;
    --ink:#111111;
    --text:#222222;
    --photo-light:#d9dbde;
    --photo-mid:#a9adb2;
    --skin-tone:#e8a58c;
  }
  *{margin:0;padding:0;box-sizing:border-box}
  html,body{width:1089px;height:1200px;overflow:hidden}
  body{background:var(--backdrop);font-family:"Open Sans",Arial,sans-serif;color:var(--text);position:relative}
  .flyer{position:absolute;left:206px;top:128px;width:719px;height:930px;background:linear-gradient(180deg,var(--paper) 45%,var(--paper-shade) 100%);overflow:hidden;box-shadow:0 4px 14px rgba(0,0,0,.45)}
  .flyer-art{position:absolute;left:0;top:0;width:719px;height:930px}
  .abs{position:absolute}
  .headline{font-family:"Oswald",Arial,sans-serif;text-transform:uppercase;text-align:right}
  .enjoy{right:29px;top:34px;font-size:84px;font-weight:600;color:#fff;line-height:1;letter-spacing:1px;text-shadow:0 2px 3px rgba(0,0,0,.3)}
  .brand-new{right:29px;top:138px;font-size:29px;font-weight:500;color:var(--ink);line-height:1}
  .product-bar{left:468px;top:191px;width:251px;height:35px;background:var(--ink);clip-path:polygon(4% 0,100% 0,100% 100%,0 100%)}
  .product-name{right:29px;top:190px;font-size:30px;font-weight:500;color:#fff;line-height:36px;letter-spacing:.5px}
  .tagline{right:24px;top:241px;font-size:18.5px;line-height:20.5px;color:#fff;text-align:right;font-weight:400}
  .code-field{left:333px;top:441px;width:360px;height:31px;border:1.5px solid #9a9a9a;border-radius:16px;background:#fff}
  .intro{left:232px;top:486px;width:458px;font-size:12px;line-height:18px;font-style:italic;font-weight:700;text-align:right;color:var(--ink)}
  .tab{font-family:"Oswald",Arial,sans-serif;color:#fff;font-size:19px;font-weight:500;line-height:25px;padding-left:36px;text-transform:uppercase}
  .tab-features{left:0;top:558px;width:172px;height:25px;background:#2a2a2a;clip-path:polygon(0 0,92% 0,100% 100%,0 100%)}
  .tab-how{left:0;top:707px;width:252px;height:25px;background:var(--red);clip-path:polygon(0 0,100% 0,93% 100%,0 100%)}
  .tab-say{left:400px;top:707px;width:277px;height:25px;background:var(--red);padding-left:29px;clip-path:polygon(4% 0,100% 0,96% 100%,0 100%)}
  .features{left:34px;top:591px;width:670px;display:grid;grid-template-columns:250px 239px 181px;row-gap:4px;list-style:none}
  .features li{font-size:15px;line-height:20.5px;color:var(--ink);display:flex;align-items:center;gap:9px}
  .tick{width:11px;height:11px;flex:none}
  .how-copy{left:33px;top:742px;width:350px;font-size:11.3px;line-height:14.6px;text-align:justify;color:var(--ink)}
  .quote{left:418px;top:739px;width:270px;font-size:11.3px;line-height:16px;color:var(--ink)}
  .quote-mark{font-family:Georgia,serif;font-size:36px;font-weight:700;line-height:10px;vertical-align:-12px;color:#333;margin-right:4px}
  .quote-author{font-weight:700;margin-top:6px;display:block}
  .certificate{left:0;top:854px;width:330px;height:76px;background:linear-gradient(90deg,var(--red-deep),var(--red));clip-path:polygon(0 0,96% 0,100% 100%,0 100%)}
  .cert-text{left:0;top:868px;width:284px;text-align:center;font-family:"Oswald",Arial,sans-serif;font-size:14.5px;line-height:27px;color:#fff;letter-spacing:.5px}
  .footer-dark{left:323px;top:854px;width:396px;height:76px;background:linear-gradient(90deg,#1a1a1a,#2e2e2e);clip-path:polygon(0 0,100% 0,100% 100%,6% 100%)}
  .cta{left:391px;top:834px;width:310px;height:43px;background:var(--red);clip-path:polygon(3% 0,100% 0,97% 100%,0 100%);font-family:"Oswald",Arial,sans-serif;color:#fff;font-size:13.5px;line-height:18px;text-align:center;padding-top:4px;letter-spacing:.3px;text-transform:uppercase;font-weight:500}
  .site{left:405px;top:885px;font-family:"Oswald",Arial,sans-serif;color:#fff;font-size:16px;line-height:22px;font-weight:500;letter-spacing:.8px;display:flex;align-items:center;gap:10px}
  .site small{font-size:12px}
  .globe{width:13px;height:13px}
  .terms{left:462px;top:910px;font-size:7.6px;color:#fff}
</style>
</head>
<body>
<main class="flyer">
  <svg class="flyer-art" viewBox="0 0 719 930" aria-hidden="false">
    <defs>
      <linearGradient id="photoTone" x1="0" y1="0" x2="1" y2="1">
        <stop offset="0" stop-color="var(--photo-light)"/>
        <stop offset=".55" stop-color="var(--skin-tone)"/>
        <stop offset="1" stop-color="var(--photo-mid)"/>
      </linearGradient>
      <linearGradient id="redPanel" x1="0" y1="0" x2="1" y2="1">
        <stop offset="0" stop-color="#e0262c"/>
        <stop offset=".6" stop-color="#b5141a"/>
        <stop offset="1" stop-color="#7d0a0e"/>
      </linearGradient>
      <radialGradient id="insetTone" cx=".5" cy=".5" r=".6">
        <stop offset="0" stop-color="#3a3d42"/>
        <stop offset=".55" stop-color="#c9a090"/>
        <stop offset="1" stop-color="#8d9196"/>
      </radialGradient>
    </defs>
    <rect x="0" y="0" width="719" height="470" fill="url(#photoTone)" role="img" aria-label="Photo of a smiling runner in an orange tank top checking her black smartwatch"/>
    <path d="M345,0 L719,0 L719,330 C620,400 480,428 395,422 C470,380 522,300 526,210 C530,120 455,40 345,0 Z" fill="url(#redPanel)"/>
    <path d="M719,318 L719,430 C680,405 610,398 560,404 C630,392 685,360 719,318 Z" fill="#111"/>
    <path d="M0,430 C120,470 280,455 420,440 C550,428 650,420 719,432 L719,930 L0,930 Z" fill="#fff" opacity=".97"/>
    <path d="M0,430 C120,470 280,455 420,440 C550,428 650,420 719,432 L719,930 L0,930 Z" fill="url(#paperFade)" opacity="0"/>
    <circle cx="128" cy="418" r="101" fill="var(--red-deep)"/>
    <circle cx="128" cy="418" r="88" fill="url(#insetTone)" role="img" aria-label="Close-up photo of a black smartwatch on a wrist showing a heart rate reading"/>
  </svg>

  <h1 class="abs headline enjoy">Enjoy</h1>
  <p class="abs headline brand-new">Your Brand New</p>
  <div class="abs product-bar"></div>
  <h2 class="abs headline product-name">Smartwatch</h2>
  <p class="abs tagline">Take Control Of Your Life<br>With Your New Smart<br>Fitness Watch</p>

  <div class="abs code-field"></div>
  <p class="abs intro">Congratulations, you have been rewarded with a Brand New Smart Fitness Watch shipped right to your door. Just pay shipping and handling. Your new Smart Fitness Watch has these features: sport mode, pedometer, distance, calorie, heartrate, blood pressure, stopwatch, sleep monitoring, phone locator, reminders, remote camera, an alarm clock and much more!</p>

  <h3 class="abs tab tab-features">Features</h3>
  <ul class="abs features">
    <li><svg class="tick" viewBox="0 0 12 12"><circle cx="6" cy="6" r="5" fill="none" stroke="#c4161c" stroke-width="1.6"/><path d="M3.6 6.2l1.7 1.6 3.1-3.3" fill="none" stroke="#c4161c" stroke-width="1.6"/></svg>Pedometer</li>
    <li><svg class="tick" viewBox="0 0 12 12"><circle cx="6" cy="6" r="5" fill="none" stroke="#c4161c" stroke-width="1.6"/><path d="M3.6 6.2l1.7 1.6 3.1-3.3" fill="none" stroke="#c4161c" stroke-width="1.6"/></svg>Distance Tracker</li>
    <li><svg class="tick" viewBox="0 0 12 12"><circle cx="6" cy="6" r="5" fill="none" stroke="#c4161c" stroke-width="1.6"/><path d="M3.6 6.2l1.7 1.6 3.1-3.3" fill="none" stroke="#c4161c" stroke-width="1.6"/></svg>Reminders Feature</li>
    <li><svg class="tick" viewBox="0 0 12 12"><circle cx="6" cy="6" r="5" fill="none" stroke="#c4161c" stroke-width="1.6"/><path d="M3.6 6.2l1.7 1.6 3.1-3.3" fill="none" stroke="#c4161c" stroke-width="1.6"/></svg>Calorie Counter</li>
    <li><svg class="tick" viewBox="0 0 12 12"><circle cx="6" cy="6" r="5" fill="none" stroke="#c4161c" stroke-width="1.6"/><path d="M3.6 6.2l1.7 1.6 3.1-3.3" fill="none" stroke="#c4161c" stroke-width="1.6"/></svg>Heart Rate Monitor</li>
    <li><svg class="tick" viewBox="0 0 12 12"><circle cx="6" cy="6" r="5" fill="none" stroke="#c4161c" stroke-width="1.6"/><path d="M3.6 6.2l1.7 1.6 3.1-3.3" fill="none" stroke="#c4161c" stroke-width="1.6"/></svg>Remote Camera</li>
    <li><svg class="tick" viewBox="0 0 12 12"><circle cx="6" cy="6" r="5" fill="none" stroke="#c4161c" stroke-width="1.6"/><path d="M3.6 6.2l1.7 1.6 3.1-3.3" fill="none" stroke="#c4161c" stroke-width="1.6"/></svg>Blood Pressure Monitor</li>
    <li><svg class="tick" viewBox="0 0 12 12"><circle cx="6" cy="6" r="5" fill="none" stroke="#c4161c" stroke-width="1.6"/><path d="M3.6 6.2l1.7 1.6 3.1-3.3" fill="none" stroke="#c4161c" stroke-width="1.6"/></svg>Stopwatch</li>
    <li><svg class="tick" viewBox="0 0 12 12"><circle cx="6" cy="6" r="5" fill="none" stroke="#c4161c" stroke-width="1.6"/><path d="M3.6 6.2l1.7 1.6 3.1-3.3" fill="none" stroke="#c4161c" stroke-width="1.6"/></svg>Alarm Clock</li>
    <li><svg class="tick" viewBox="0 0 12 12"><circle cx="6" cy="6" r="5" fill="none" stroke="#c4161c" stroke-width="1.6"/><path d="M3.6 6.2l1.7 1.6 3.1-3.3" fill="none" stroke="#c4161c" stroke-width="1.6"/></svg>Sleep Monitoring</li>
    <li><svg class="tick" viewBox="0 0 12 12"><circle cx="6" cy="6" r="5" fill="none" stroke="#c4161c" stroke-width="1.6"/><path d="M3.6 6.2l1.7 1.6 3.1-3.3" fill="none" stroke="#c4161c" stroke-width="1.6"/></svg>Phone Locator</li>
    <li><svg class="tick" viewBox="0 0 12 12"><circle cx="6" cy="6" r="5" fill="none" stroke="#c4161c" stroke-width="1.6"/><path d="M3.6 6.2l1.7 1.6 3.1-3.3" fill="none" stroke="#c4161c" stroke-width="1.6"/></svg>Waterproof</li>
  </ul>

  <h3 class="abs tab tab-how">How Can We Do This?</h3>
  <p class="abs how-copy">We have a couple retail partners that we team up with to "crowd purchase" huge shipping containers that hold 10's of thousands of electronic products at 80-90% off retail. We simply pass our savings on to you as we do not profit from our electronic products. You are basically able to "piggy back" on our partnerships and buying power to get an attractive electronic premium for a fraction of the retail cost.</p>

  <h3 class="abs tab tab-say">What Other Say</h3>
  <blockquote class="abs quote"><span class="quote-mark">“</span>Are you sure this is not a Norvex Orbit Smartwatch in DISGUISE???? I love mine."<span class="quote-author">Dale M. Atlantic City, NJ</span></blockquote>

  <div class="abs certificate"></div>
  <p class="abs cert-text">CERTIFICATE ID: 91772-89218<br>EXPIRES: 10/03/2020</p>
  <div class="abs footer-dark"></div>
  <p class="abs cta">View all the details of this special offer<br>and redeem online at</p>
  <p class="abs site"><svg class="globe" viewBox="0 0 14 14"><circle cx="7" cy="7" r="6" fill="none" stroke="#fff" stroke-width="1.3"/><ellipse cx="7" cy="7" rx="2.6" ry="6" fill="none" stroke="#fff" stroke-width="1.1"/><path d="M1 7h12M2 4h10M2 10h10" stroke="#fff" stroke-width="1"/></svg><span>www.PERKSANDBONUSES<small>.com</small></span></p>
  <p class="abs terms">*Terms and Conditions apply see website for details</p>
</main>
</body>
</html>
```